Label Design for a New Alcoholized Root Beer

Create a design for a new alcoholized root beer. This is a new product category in the USA growing very rapidly. Root Beer is a popular flavor of Cola, but recently, beer manufacturers have added alcohol to it and have created a new product that has gained traction on the market at a tremendous rate.

Root Beer is vintage product that has been around for a hundred years. Consumers of this product are mostly male between the age of 30 to 45. They purchase this product for its nostalgia and vintage look and taste.

This product will be in a standard 355 mL brown bottle.

It is 5.9% abv.

The name of the product is ''Corvel's Hard Root Beer''.

We have uploaded some pictures of traditional root beers to give you an idea of the feel we want our product to have and also, the bottle the product will be filled in.

Target Market(s)

Consumers are male 30-45, same market as craft beer consumers

Industry/Entity Type

Product

Requirements
Must have
• Design must have a vintage feel to it

```html
<!DOCTYPE html>
<html lang="en">
<head>
<meta charset="utf-8">
<title>Corvel's Hard Root Beer – Bottle Label</title>
<link rel="stylesheet" href="https://fonts.googleapis.com/css2?family=Lobster&family=Federo&family=Limelight&family=Playfair+Display:wght@400&display=swap">
<style>
  :root {
    --page-bg: #efe7de;
    --label-cream: #fcf1e8;
    --label-peach: #f2d2c0;
    --label-border: #c88a5c;
    --label-border-dark: #a8683f;
    --script-red: #d6553a;
    --banner-olive: #7b6a4b;
    --banner-text: #f1d27a;
    --beer-gold: #e3a24a;
    --ink-brown: #6a4a35;
  }
  * { margin: 0; padding: 0; box-sizing: border-box; }
  html, body {
    width: 894px;
    height: 1200px;
    overflow: hidden;
    background: var(--page-bg);
  }
  .canvas {
    position: relative;
    width: 894px;
    height: 1200px;
  }
  .label {
    position: absolute;
    left: 147px;
    top: 195px;
    width: 600px;
    height: 810px;
  }
  .label-shape {
    position: absolute;
    inset: 0;
  }
  .label-abv {
    position: absolute;
    top: 40px;
    width: 100%;
    text-align: center;
    font-family: "Playfair Display", serif;
    font-size: 20px;
    color: var(--ink-brown);
    letter-spacing: 1px;
  }
  .label-laurel {
    position: absolute;
    left: 165px;
    top: 138px;
    width: 270px;
    height: 36px;
    border-radius: 18px;
    background: var(--script-red);
  }
  .label-name {
    position: absolute;
    top: 196px;
    width: 100%;
    text-align: center;
    font-family: "Lobster", cursive;
    font-size: 118px;
    line-height: 1.2;
    color: var(--script-red);
  }
  .label-style {
    position: absolute;
    top: 418px;
    width: 100%;
    text-align: center;
    font-family: "Federo", sans-serif;
    font-size: 62px;
    line-height: 1;
    color: var(--banner-text);
    letter-spacing: 2px;
    transform: rotate(-4deg);
  }
  .label-beer {
    position: absolute;
    top: 592px;
    width: 100%;
    text-align: center;
    font-family: "Limelight", sans-serif;
    font-size: 84px;
    line-height: 1;
    color: var(--beer-gold);
    letter-spacing: 6px;
  }
  .label-stars {
    position: absolute;
    left: 255px;
    top: 728px;
    width: 90px;
    height: 22px;
    border-radius: 11px;
    background: var(--beer-gold);
  }
</style>
</head>
<body>
<main class="canvas">
  <section class="label">
    <svg class="label-shape" width="600" height="810" viewBox="0 0 600 810" aria-hidden="true">
      <defs>
        <radialGradient id="label-glow" cx="50%" cy="55%" r="60%">
          <stop offset="0%" stop-color="var(--label-cream)"/>
          <stop offset="100%" stop-color="var(--label-peach)"/>
        </radialGradient>
      </defs>
      <path d="M0,120 L0,620 L300,800 L600,620 L600,120 L540,60 Q300,0 60,60 Z"
            fill="var(--label-border)"/>
      <path d="M14,126 L14,612 L300,784 L586,612 L586,126 L533,73 Q300,16 67,73 Z"
            fill="url(#label-glow)" stroke="var(--label-border-dark)" stroke-width="2"/>
      <path d="M0,440 C150,370 320,480 600,395 L600,480 C320,560 150,450 0,520 Z"
            fill="var(--banner-olive)"/>
    </svg>
    <p class="label-abv">5.9% abv</p>
    <div class="label-laurel" role="img" aria-label="Laurel branch ornament"></div>
    <h1 class="label-name">Corvel's</h1>
    <p class="label-style">HARD ROOT</p>
    <p class="label-beer">BEER</p>
    <div class="label-stars" role="img" aria-label="Row of three small stars"></div>
  </section>
</main>
</body>
</html>
```